Luxury Brand Coffee Table Book Template

Overview:
We are creating a premium, 28-page coffee table book to accompany every bespoke jewelry piece handcrafted by Vellmoor Jewelry. This book serves as an heirloom that documents the story, design, and craftsmanship behind each custom piece, culminating in a powerful legacy statement. We need a refined, luxurious, and masculine layout template that can be updated for each new customer.
**All reference files (images, logos, copy for pages, etc.) are included in the .zip file.
Deliverables:
Print-ready 28-page InDesign or editable template file
Front and back cover design
Consistent typography and page layouts based on our outlined structure
Design system that allows for easy photo and text updates per client
Specs:
Size: 8.1 x 10.6 in, Portrait Orientation
Cover: Black linen hardcover with gold foil stamped name or crest (simulated in mockup)
Interior: Deep matte photo paper feel – minimalistic, clean layout with generous whitespace
Color Palette: Black, white, and gold
Style: Bold, masculine, timeless, high-luxury (think Karvane Studio x Dellbrook & Co.)
See the attached 28-page outline. Please use stock image placeholders for now.
Target Market(s)
Affluent Men & Women age 35-65
Industry/Entity Type
Luxury Retail Jewelry
Font styles to use
Other font styles liked:
- I really like Trajan Pro 3, but open to suggestions, as well as a mixture of Serif and Sans Serif fonts
Look and feel
Each slider illustrates characteristics of the customer's brand and the style your logo design should communicate.

```html
<!DOCTYPE html>
<html lang="en">
<head>
<meta charset="utf-8">
<title>Vellmoor Jewelry – Coffee Table Book Template</title>
<link rel="stylesheet" href="https://fonts.googleapis.com/css2?family=Oswald:wght@600&family=Roboto:wght@300;400&family=Lora:wght@400;600&family=Great+Vibes&display=swap">
<style>
  :root{
    --backdrop:#c8c9cb;
    --paper:#ffffff;
    --ink:#111111;
    --body:#3a3a3a;
    --muted:#555555;
    --gold:#e9b127;
    --quote-bg:#f3f2ef;
    --tab:#ececec;
    --black:#000000;
  }
  *{margin:0;padding:0;box-sizing:border-box}
  html,body{width:1200px;height:3012px;overflow:hidden}
  body{background:var(--backdrop);position:relative;font-family:"Roboto",Arial,sans-serif;color:var(--body)}
  .abs{position:absolute}

  /* Cover */
  .cover{left:335px;top:74px;width:506px;height:666px;background:var(--black)}
  .cover-brand{position:absolute;left:85px;top:210px;display:flex;align-items:center;gap:12px;color:#fff;font-family:"Lora",Georgia,serif;font-weight:600}
  .cover-brand .mark{width:56px;height:56px;border:3px solid #fff;border-radius:50%}
  .cover-brand .name{line-height:1}
  .cover-brand .name span{display:block}
  .cover-brand .line1{font-size:30px;letter-spacing:1px}
  .cover-brand .line2{font-size:14px;letter-spacing:19px;margin-top:6px}
  .cover-owner{position:absolute;left:0;right:0;top:565px;text-align:center;font-family:"Great Vibes",cursive;font-size:44px;color:var(--gold)}

  /* Spreads */
  .spread{background:var(--paper);overflow:hidden}
  .page{position:absolute;top:0;bottom:0;background:var(--paper)}
  .page-left::after{content:"";position:absolute;top:0;right:0;bottom:0;width:70px;background:linear-gradient(90deg,rgba(0,0,0,0),rgba(0,0,0,.18));pointer-events:none}
  .page-right::before{content:"";position:absolute;top:0;left:0;bottom:0;width:60px;background:linear-gradient(90deg,rgba(0,0,0,.22),rgba(0,0,0,0));pointer-events:none;z-index:2}
  .photo{position:absolute}
  .folio{position:absolute;bottom:0;width:30px;height:30px;background:var(--tab);font-family:"Oswald",sans-serif;font-weight:600;font-size:12px;font-weight:400;color:#333;display:flex;align-items:center;justify-content:center;z-index:3}
  .section-bar{position:absolute;background:var(--black);width:13px}
  .section-title{position:absolute;font-family:"Oswald",Impact,sans-serif;font-weight:600;font-size:33px;color:var(--ink);line-height:1;letter-spacing:.3px}
  .body-copy{font-size:13px;line-height:17.8px;font-weight:300;color:var(--body)}
  .serif-head{font-family:"Lora",Georgia,serif;font-size:15px;color:var(--ink)}

  /* Story */
  .story-copy{position:absolute;left:41px;top:79px;width:395px;font-size:13.2px;line-height:17.8px;font-weight:300;color:#333}
  .quote-box{position:absolute;left:176px;top:300px;width:330px;height:187px;background:var(--quote-bg)}
  .quote-mark{position:absolute;left:18px;top:12px;font-family:"Lora",serif;font-weight:600;font-size:22px;color:#222}
  .quote-text{position:absolute;left:35px;top:40px;width:270px;font-family:"Lora",Georgia,serif;font-size:11px;line-height:15px;color:#222}
  .quote-sign{position:absolute;left:35px;top:136px;font-family:"Great Vibes",cursive;font-size:22px;color:#222}

  /* Design */
  .rule{position:absolute;background:#222}
  .design-block{position:absolute;width:378px}
  .design-block p{text-align:justify;font-size:12px;line-height:17px;font-weight:300;color:#333;margin-top:8px}
  .design-block.center{text-align:center}
  .design-block.center p{text-align:center}
  .design-block.right{text-align:right}
  .design-block.right p{text-align-last:right}

  /* Gallery */
  .item-head{position:absolute;font-family:"Lora",Georgia,serif;font-size:14.5px;color:var(--ink)}
  .item-copy{position:absolute;width:210px;font-size:11.2px;line-height:14px;font-weight:300;color:#333}
  .shot-grey{background:radial-gradient(ellipse at 50% 50%,#a07a2c 0%,#6b5326 28%,#333 62%,#2a2a2a 100%)}
  .shot-black{background:radial-gradient(ellipse at 50% 48%,#8f7230 0%,#4a3b1d 26%,#0d0d0d 55%,#000 100%)}
</style>
</head>
<body>

<!-- Cover -->
<section class="abs cover" aria-label="Front cover">
  <div class="cover-brand">
    <div class="mark"></div>
    <div class="name"><span class="line1">VELLMOOR</span><span class="line2">JEWELRY</span></div>
  </div>
  <div class="cover-owner">Elias Varren</div>
</section>

<!-- Spread: Story -->
<section class="abs spread" style="left:94px;top:808px;width:1011px;height:667px" aria-label="Story spread">
  <div class="page page-left" style="left:0;width:505px">
    <div class="photo" role="img" aria-label="Gold signet ring with enamel crest and knight helm on a white reflective surface" style="left:0;top:0;width:505px;height:667px;background:radial-gradient(ellipse at 45% 48%,#b98a2e 0%,#c99f55 22%,#e8dcc6 45%,#f6f4f1 70%,#ffffff 100%)"></div>
    <div class="folio" style="right:2px">01</div>
  </div>
  <div class="page page-right" style="left:505px;width:506px">
    <div class="section-bar" style="left:0;top:27px;height:40px"></div>
    <h2 class="section-title" style="left:36px;top:32px">STORY</h2>
    <p class="story-copy">Lorem ipsum dolor sit amet, consectetur adipiscing elit, sed do eiusmod tempor incididunt ut labore et dolore magna aliqua. Ut enim ad minim veniam, quis nostrud exercitation ullamco laboris nisi ut aliquip ex ea commodo consequat. Duis aute irure dolor in reprehenderit in voluptate velit esse cillum dolore eu fugiat nulla pariatur. Excepteur sint occaecat cupidatat non proident, sunt in culpa qui officia deserunt mollit anim id est laborum</p>
    <div class="quote-box">
      <div class="quote-mark">&ldquo;</div>
      <p class="quote-text">Sed ut perspiciatis unde omnis iste natus error sit voluptatem accusantium doloremque laudantium, totam rem aperiam, eaque ipsa quae ab illo inventore veritatis et quasi architecto beatae vitae dicta sunt explicabo. Nemo enim ipsam voluptatem quia voluptas sit aspernatur aut odit aut fugit</p>
      <div class="quote-sign">Elias Varren</div>
    </div>
    <div class="folio" style="right:0">02</div>
  </div>
</section>

<!-- Spread: Design -->
<section class="abs spread" style="left:98px;top:1538px;width:1010px;height:667px" aria-label="Design spread">
  <div class="page page-left" style="left:0;width:503px">
    <div class="photo" role="img" aria-label="Gloved hands polishing a gold medallion pendant on a workbench" style="left:0;top:0;width:503px;height:667px;background:radial-gradient(ellipse at 38% 48%,#b89548 0%,#7a6a58 18%,#4f4741 40%,#2a2522 62%,#6b4a30 86%,#8a6440 100%)"></div>
    <div class="folio" style="right:2px">03</div>
  </div>
  <div class="page page-right" style="left:503px;width:507px">
    <div class="section-bar" style="left:0;top:21px;height:41px"></div>
    <h2 class="section-title" style="left:27px;top:26px">DESIGN</h2>

    <div class="rule" style="left:32px;top:91px;width:1px;height:158px"></div>
    <div class="rule" style="left:32px;top:249px;width:434px;height:1px"></div>
    <div class="rule" style="left:465px;top:249px;width:1px;height:178px"></div>
    <div class="rule" style="left:32px;top:427px;width:434px;height:1px"></div>
    <div class="rule" style="left:32px;top:427px;width:1px;height:175px"></div>

    <div class="design-block" style="left:59px;top:93px">
      <h3 class="serif-head">Lorem ipsum</h3>
      <p>Sed ut perspiciatis unde omnis iste natus error sit voluptatem accusantium doloremque laudantium, totam rem aperiam, eaque ipsa quae ab illo inventore veritatis et quasi architecto beatae vitae dicta sunt explicabo. Nemo enim ipsam voluptatem quia voluptas sit aspernatur aut odit aut fugit, sed quia consequuntur magni dolores eos qui ratione voluptatem sequi nesciunt. Neque porro quisquam est, qui dolorem ipsum quia dolor sit</p>
    </div>
    <div class="design-block center" style="left:60px;top:286px">
      <h3 class="serif-head">Lorem ipsum</h3>
      <p style="margin-top:14px">Sed ut perspiciatis unde omnis iste natus error sit voluptatem accusantium doloremque laudantium, totam rem aperiam, eaque ipsa quae ab illo inventore veritatis et quasi architecto beatae vitae dicta sunt explicabo. Nemo enim ipsam voluptatem quia voluptas sit aspernatur .</p>
    </div>
    <div class="design-block right" style="left:61px;top:472px">
      <h3 class="serif-head">Lorem ipsum</h3>
      <p style="margin-top:12px">Sed ut perspiciatis unde omnis iste natus error sit voluptatem accusantium doloremque laudantium, totam rem aperiam, eaque ipsa quae ab illo inventore veritatis et quasi architecto beatae vitae dicta sunt explicabo. Nemo enim ipsam voluptatem quia voluptas sit aspernatur aut odit aut fugit, sed quia consequuntur magni dolores eos qui ratione voluptatem sequi nesciunt. Neque porro quisquam est, qui dolorem ipsum quia dolor sit</p>
    </div>
    <div class="folio" style="right:0">04</div>
  </div>
</section>

<!-- Spread: Gallery -->
<section class="abs spread" style="left:101px;top:2283px;width:1011px;height:667px" aria-label="Gallery spread">
  <div class="page page-left" style="left:0;width:504px">
    <h3 class="item-head" style="left:25px;top:44px">Lorem ipsum</h3>
    <p class="item-copy" style="left:25px;top:69px">Lorem ipsum dolor sit amet, consectetur adipiscing elit, sed do eiusmod tempor.</p>
    <div class="photo shot-grey" role="img" aria-label="Gold crest ring with enamel shield, front view" style="left:25px;top:103px;width:208px;height:216px"></div>

    <h3 class="item-head" style="left:265px;top:23px">Lorem ipsum</h3>
    <p class="item-copy" style="left:265px;top:48px">Lorem ipsum dolor sit amet, consectetur adipiscing elit, sed do eiusmod tempor.</p>
    <div class="photo shot-grey" role="img" aria-label="Gold crest ring, side view with eagle shoulder" style="left:267px;top:88px;width:209px;height:207px"></div>

    <div class="photo shot-grey" role="img" aria-label="Gold ring with engraved silver panel, inside view" style="left:25px;top:363px;width:208px;height:207px"></div>
    <h3 class="item-head" style="left:25px;top:585px">Lorem ipsum</h3>
    <p class="item-copy" style="left:25px;top:608px">Lorem ipsum dolor sit amet, consectetur adipiscing elit, sed do eiusmod tempor.</p>

    <div class="photo shot-grey" role="img" aria-label="Crest ring top view with rose gold scrollwork" style="left:267px;top:340px;width:209px;height:207px"></div>
    <h3 class="item-head" style="left:265px;top:566px">Lorem ipsum</h3>
    <p class="item-copy" style="left:265px;top:591px">Lorem ipsum dolor sit amet, consectetur adipiscing elit, sed do eiusmod tempor.</p>

    <div class="folio" style="right:1px">05</div>
  </div>
  <div class="page page-right" style="left:504px;width:507px">
    <div class="section-bar" style="left:0;top:0;height:39px"></div>
    <h3 class="item-head" style="left:28px;top:107px">Lorem ipsum</h3>
    <p class="item-copy" style="left:28px;top:131px">Lorem ipsum dolor sit amet, consectetur adipiscing elit, sed do eiusmod tempor.</p>
    <div class="photo shot-black" role="img" aria-label="Crest ring top view on black background" style="left:245px;top:23px;width:246px;height:244px"></div>

    <div class="photo shot-black" role="img" aria-label="Gold ring with silver panel on black background" style="left:25px;top:288px;width:226px;height:227px"></div>
    <h3 class="item-head" style="left:276px;top:303px">Lorem ipsum</h3>
    <p class="item-copy" style="left:276px;top:328px">Lorem ipsum dolor sit amet, consectetur adipiscing elit, sed do eiusmod tempor.</p>
    <div class="photo shot-black" role="img" aria-label="Crest ring angled view with reflection on black background" style="left:276px;top:385px;width:210px;height:209px"></div>

    <h3 class="item-head" style="left:36px;top:533px">Lorem ipsum</h3>
    <p class="item-copy" style="left:36px;top:557px">Lorem ipsum dolor sit amet, consectetur adipiscing elit, sed do eiusmod tempor.</p>

    <div class="folio" style="right:0">06</div>
  </div>
</section>

</body>
</html>
```